Design a menu for health restaurant

A health food restaurant in Los Angeles is seeking menu design. Our foods are made from scratch using whole ingredients.
Name: Grubb Larder
Address: 1000 E 60th StLos Angeles, CA 90247
Website: www.GrubbLarder.example
We are looking for a clean and simple menu. Brand colors are white/tan, green and orange.

Please see attached excel with menu items and logo. We do not yet have prices.

Colors
f78f20
9bcb3c
ffffff
fff3d1

Requirements
Must have
• Easy to read.
Trifold menu design (front and back).
VEGAN, VEGETARIAN, GLUTEN FREE, CONTAINS NUTS symbols.
Logo.
Nice to have
• Incorporate brand colors, but still be easy to read.
We would like to use the Belco font (attached) if it works. If not we are open to a similar font that is easy to read.

Please see attached images.
We like the images and headers of OPTION 1. Would like something similar in trifold format.
We like the clean fonts of OPTION 2.

```html
<!DOCTYPE html>
<html lang="en">
<head>
<meta charset="utf-8">
<title>Grubb Larder Menu</title>
<link href="https://fonts.googleapis.com/css2?family=Montserrat:wght@200;300;400;600;700&display=swap" rel="stylesheet">
<style>
:root{
  --green:#8dc63f;
  --orange:#f78f20;
  --ink:#1d1d1b;
  --paper:#f7f8f8;
  --rule:#3a3a3a;
  --badge-v:#2f7d3a;
  --badge-vg:#8bc34a;
  --badge-gf:#f4d64a;
  --badge-n:#f2a383;
}
*{margin:0;padding:0;box-sizing:border-box}
html,body{width:1200px;height:848px;overflow:hidden;background:var(--paper)}
body{font-family:"Montserrat",sans-serif;color:var(--ink);position:relative}
.panel{position:absolute;top:0;height:848px;overflow:hidden}
.panel--left{left:0;width:400px}
.panel--middle{left:401px;width:399px;border-left:1px solid var(--rule)}
.panel--cover{left:800px;width:400px;border-left:1px solid var(--rule)}
.section-bar{position:absolute;height:4px;background:var(--green);width:131px}
.section-title{position:absolute;font-weight:200;color:var(--green);font-size:34px;line-height:1;letter-spacing:-0.5px}
.photo{position:absolute;overflow:hidden}
.photo__disc{position:absolute;border-radius:50%}
.items{position:absolute;left:31px;width:350px}
.item{margin-bottom:8.6px}
.item__head{display:flex;align-items:center;height:13.6px;font-size:12px}
.item__name{font-weight:700;letter-spacing:0.1px}
.item__price{font-weight:400;margin-left:14px}
.item__desc{font-size:8.9px;font-weight:300;line-height:11.6px}
.badges{display:flex;gap:3px;margin-left:5px}
.badge{width:11px;height:11px;border-radius:50%;font-size:5.5px;font-weight:700;display:flex;align-items:center;justify-content:center}
.badge--v{background:var(--badge-v);color:#fff}
.badge--vg{background:var(--badge-vg);color:#1d3b10}
.badge--gf{background:var(--badge-gf);color:#4a3b00}
.badge--n{background:var(--badge-n);color:#5a2414}
.legend{position:absolute;left:34px;top:816px;display:flex;gap:26px;font-size:8.5px;font-weight:400}
.legend span{display:flex;align-items:center;gap:5px}
.bottled{font-size:10px;font-weight:300;line-height:15.6px}
.bottled small{font-size:7.4px}
.cover-title{position:absolute;left:0;top:0}
.cover-art{position:absolute;left:0;top:135px;width:400px;height:500px;background:radial-gradient(ellipse at 50% 45%,#b9cf8a 0%,#d9dcc4 45%,#eef0ea 70%,var(--paper) 100%)}
.brand{position:absolute;left:0;top:600px;width:400px;display:flex;flex-direction:column;align-items:center;gap:8px}
.brand__mark{width:84px;height:84px;border-radius:50%;background:var(--orange)}
.brand__name{font-size:16px;font-weight:700;color:var(--orange)}
.site{position:absolute;left:0;top:748px;width:400px;text-align:center;font-size:22px;font-weight:700}
.address{position:absolute;left:0;top:782px;width:400px;text-align:center;font-size:18px;font-weight:300}
</style>
</head>
<body>

<section class="panel panel--left">
  <div class="photo" style="left:164px;top:24px;width:212px;height:112px">
    <div class="photo__disc" role="img" aria-label="Breakfast plate with fried eggs, spinach and tomatoes, toast on a board" style="left:34px;top:-86px;width:206px;height:206px;background:radial-gradient(circle at 60% 60%,#f6d36a 0%,#e9e3d3 35%,#8c8a84 70%,#c7c3bb 100%)"></div>
  </div>
  <div class="section-bar" style="left:31px;top:25px"></div>
  <h2 class="section-title" style="left:29px;top:49px">BREAKFAST</h2>

  <div class="items" style="top:106px">
    <div class="item"><div class="item__head"><span class="item__name">Pastries</span><span class="badges"><i class="badge badge--v">V</i></span><span class="item__price">0.00</span></div><p class="item__desc">"Croissant (regular, almond, chocolate)<br>Blueberry MuffinSuperseed Cookie"</p></div>
    <div class="item"><div class="item__head"><span class="item__name">Parfait</span><span class="badges"><i class="badge badge--v">V</i></span><span class="item__price">0.00</span></div><p class="item__desc">Fresh strawberries and blueberries on yogurt and muesli and topped with honey drizzle.</p></div>
    <div class="item"><div class="item__head"><span class="item__name">Avocado Super Toast</span><span class="badges"><i class="badge badge--vg">VG</i></span><span class="item__price">0.00</span></div><p class="item__desc">Avocado Mash, Tomato, Basil, Ground Flax, Hemp Seed, Chickpeas, and Moringa Powder on Whole Wheat Bread.</p></div>
    <div class="item"><div class="item__head"><span class="item__name">Brunch Burger</span><span class="item__price" style="margin-left:40px">0.00</span></div><p class="item__desc">House seasoned beef burger topped with an over medium egg, red leaf lettuce, tomato, housemade pickles and Larder Sauce on a bun.</p></div>
    <div class="item"><div class="item__head"><span class="item__name">Breakfast Sammy</span><span class="item__price" style="margin-left:40px">0.00</span></div><p class="item__desc">Your choice of over medium egg or tofu steak with guacamole, tomato, and Larder sauce on an English muffin. Vegan Option*</p></div>
    <div class="item"><div class="item__head"><span class="item__name">AM Burrito</span><span class="badges"><i class="badge badge--v">V</i></span><span class="item__price" style="margin-left:22px">0.00</span></div><p class="item__desc">Scrambled eggs, onion, red bell pepper, black beans, housemade salsa, yogurt, and pepper jack cheese in a tortilla.</p></div>
  </div>

  <div class="photo" style="left:164px;top:401px;width:212px;height:110px">
    <div class="photo__disc" role="img" aria-label="Smoothie bowl topped with blueberries, banana slices and granola" style="left:30px;top:-90px;width:200px;height:200px;background:radial-gradient(circle at 45% 50%,#d9558b 0%,#e9c9a0 35%,#e6e8ec 65%,#f1f2f4 100%)"></div>
  </div>
  <div class="section-bar" style="left:31px;top:401px"></div>
  <h2 class="section-title" style="left:29px;top:428px">SMOOTHIES</h2>

  <div class="items" style="top:484px">
    <div class="item"><div class="item__head"><span class="item__name">Green Machine Smoothie</span><span class="badges"><i class="badge badge--vg">VG</i><i class="badge badge--n">N</i><i class="badge badge--gf">GF</i></span><span class="item__price">0.00</span></div><p class="item__desc">Romaine, spinach, banana, mango, pineapple,<br>flaxmilk, spirulina, almond butter</p></div>
    <div class="item"><div class="item__head"><span class="item__name">Acai Smoothie</span><span class="badges"><i class="badge badge--vg">VG</i><i class="badge badge--n">N</i><i class="badge badge--gf">GF</i></span><span class="item__price">0.00</span></div><p class="item__desc">Acai, blueberries, banana, pineapple, Macqui berry, flaxmilk, almond butter</p></div>
    <div class="item"><div class="item__head"><span class="item__name">Mango Smoothie</span><span class="badges"><i class="badge badge--vg">VG</i><i class="badge badge--gf">GF</i></span><span class="item__price" style="margin-left:24px">0.00</span></div><p class="item__desc">Mango, flaxmilk, banan, hemp seeds</p></div>
  </div>

  <div class="photo" style="left:162px;top:617px;width:214px;height:110px">
    <div class="photo__disc" role="img" aria-label="Bowl of golden squash soup with parsley on a dark wooden table" style="left:0;top:-106px;width:216px;height:216px;background:radial-gradient(circle at 30% 40%,#f3a640 0%,#e8d7b8 25%,#6b4a33 50%,#3e2a1e 100%)"></div>
  </div>
  <div class="section-bar" style="left:31px;top:617px"></div>
  <h2 class="section-title" style="left:29px;top:645px">SOUPS</h2>

  <div class="items" style="top:700px">
    <div class="item"><div class="item__head"><span class="item__name">Chicken Noodle</span><span class="badges"><i class="badge badge--gf">GF</i></span><span class="item__price" style="margin-left:28px">0.00</span></div><p class="item__desc">Chicken, egg noodles, root vegetables,<br>oregano &amp; peppercorns.</p></div>
    <div class="item"><div class="item__head"><span class="item__name">Larder Chili</span><span class="badges"><i class="badge badge--gf">GF</i></span><span class="item__price" style="margin-left:28px">0.00</span></div><p class="item__desc">Chicken, onions, bell peppers, jalapeños, black &amp; kidney beans, and tomato.</p></div>
    <div class="item"><div class="item__head"><span class="item__name">Seasonal Rotating (Butternut Squash Soup)</span><span class="badges"><i class="badge badge--vg">VG</i><i class="badge badge--gf">GF</i></span><span class="item__price" style="margin-left:8px">0.00</span></div><p class="item__desc">Butternut squash blended with warm spices, and coconut milk.</p></div>
  </div>

  <div class="legend">
    <span><i class="badge badge--v">V</i>Vegetarian</span>
    <span><i class="badge badge--vg">VG</i>Vegan</span>
    <span><i class="badge badge--gf">GF</i>Gluten Free</span>
    <span><i class="badge badge--n">N</i>Contains Nuts</span>
  </div>
</section>

<section class="panel panel--middle">
  <div class="photo__disc" role="img" aria-label="Two glasses of fresh orange and mango juice with straws by a pool" style="left:80px;top:47px;width:362px;height:362px;background:radial-gradient(circle at 50% 55%,#f6c21c 0%,#f2a531 30%,#9fc46a 60%,#e3eee4 100%)"></div>
  <div class="section-bar" style="left:27px;top:344px;width:142px"></div>
  <h2 class="section-title" style="left:25px;top:363px">DRINKS</h2>

  <div class="items" style="left:26px;top:416px;width:360px">
    <div class="item"><div class="item__head"><span class="item__name">Coffee</span><span class="item__price" style="margin-left:40px">0.00</span></div><p class="item__desc">We proudly serve Tidewell Coffee, a local roaster.</p></div>
    <div class="item"><div class="item__head"><span class="item__name">Power Date Shake</span><span class="badges"><i class="badge badge--vg">VG</i><i class="badge badge--gf">GF</i></span><span class="item__price">0.00</span></div><p class="item__desc">Ice-blended energy smoothie featuring dates and coffee.</p></div>
    <div class="item"><div class="item__head"><span class="item__name">Heart Beet Juice</span><span class="badges"><i class="badge badge--vg">VG</i><i class="badge badge--gf">GF</i></span><span class="item__price">0.00</span></div><p class="item__desc">Red beet, apple, carrot, ginger, parsley, and lemon.</p></div>
    <div class="item"><div class="item__head"><span class="item__name">Green Leafy Juice</span><span class="badges"><i class="badge badge--vg">VG</i><i class="badge badge--gf">GF</i></span><span class="item__price">0.00</span></div><p class="item__desc">Spinach, kale, cucumber, apple, and oranges.</p></div>
    <div class="item"><div class="item__head"><span class="item__name">Orange Turmeric Juice</span><span class="badges"><i class="badge badge--vg">VG</i><i class="badge badge--gf">GF</i></span><span class="item__price">0.00</span></div><p class="item__desc">Turmeric, ginger, lemon, carrot, and orange topped with cracked black pepper.</p></div>
    <div class="item"><div class="item__head"><span class="item__name">Fireshot</span><span class="badges"><i class="badge badge--vg">VG</i><i class="badge badge--gf">GF</i></span><span class="item__price">0.00</span></div><p class="item__desc">Ginger and lemon shot topped with cayenne.</p></div>
    <div class="item"><div class="item__head"><span class="item__name">Lemonade</span><span class="item__price" style="margin-left:40px">0.00</span></div><p class="item__desc">House Made Lemonade. Choice of unsweetened or agave sweetened in Regular, Raspberry, and Lavender flavors.</p></div>
    <div class="item"><div class="item__head"><span class="item__name">Tea</span><span class="item__price" style="margin-left:40px">0.00</span></div><p class="item__desc">Hot or iced.</p></div>
    <div class="item" style="margin-bottom:2px"><div class="item__head"><span class="item__name">Bottled Drinks</span></div></div>
    <div class="bottled">
      <p>Brightroot kombucha <small>(Harmony Trilogy, Harmony Gingerberry, Harmony Mango)</small> 0.00</p>
      <p>Fizzwell <small>(Orange Mango, Lemon, Grapefruit)Palm Grove Original)</small> 0.00</p>
      <p>Sparkling Water <small>(Clearspring)</small> 0.00</p>
      <p>Still Water <small>(Clearspring)</small> 0.00</p>
    </div>
  </div>
</section>

<section class="panel panel--cover">
  <div class="cover-art" role="img" aria-label="Scattered fresh produce: avocado halves, mushrooms, garlic cloves, spinach leaves, lettuce and cherry tomatoes"></div>
  <svg class="cover-title" width="400" height="120" viewBox="0 0 400 120" aria-label="Menu">
    <text x="-2" y="103" font-family="Montserrat, sans-serif" font-weight="200" font-size="166" fill="#f78f20" textLength="420" lengthAdjust="spacingAndGlyphs">MENU</text>
  </svg>
  <div class="brand">
    <div class="brand__mark"></div>
    <div class="brand__name">Grubb Larder</div>
  </div>
  <p class="site">GrubbLarder.example</p>
  <p class="address">2417 W 83rd St Los Angeles, CA 90247</p>
</section>

</body>
</html>
```